Harborline Talent IT Recruiting firm needs a business card design for Recruiters, Sourcers, and Account

We need business cards that allow us to change all contact info, names, titles (Recruiter, Sourcer, Account Manager, Director, CEO, etc) per person since we have three offices, in three cities, Phoenix, Austin, and Las Vegas. We do recruiting and contractors for IT positions (Developers, Architects, Software Engineers, Security Engineers, Help Desk, DBAs, PMs, Scrum Masters, etc.) Our client companies are very diverse from Crestline 250 to silicone Valley type start-ups.

So, while we what hip, techie, and quirky, it still needs to be professional. Primary color we use is blue, with silver as a secondary color.

Target Market(s)

IT, Technology

Industry/Entity Type

Business

Contact Information for Business Card

Company name: Harborline Talent, Inc.
Website: www.harborlinetalent-example.com
Logos for ProCircle, Quillo, and Roomwall

Name, Title, Office Number, Cell Number, email

Font styles to use
Serif
Sans Serif

Colors
0455a3
d5d5d5

Requirements
Nice to have
• The grey I selected below is not necessary - but, would like silver included. I included a card design (File 3: HTI early trial example.jpg) that I had started on. It's very rough, and not quite what we're looking for, but what we did like is the logo, big, maybe a bit faded, off center, goes out of frame, etc. Still looking for other ideas - you are the pros! But, just an idea of a design element we liked.

```html
<!DOCTYPE html>
<html lang="en">
<head>
<meta charset="utf-8">
<title>Harborline Talent — Business Card</title>
<link rel="stylesheet" href="https://fonts.googleapis.com/css2?family=Oswald:wght@500&family=Play:wght@400;700&family=Cinzel:wght@400&display=swap">
<style>
  :root {
    --backdrop: #9a9a9a;
    --card-white: #f7f7f7;
    --card-silver: #d9d9d9;
    --brand-blue: #1f86d8;
    --brand-blue-deep: #0a62b0;
    --ink: #2b2b2b;
    --ink-soft: #4a4a4a;
    --bar-black: #1c1c1c;
    --white: #ffffff;
  }
  * { box-sizing: border-box; margin: 0; padding: 0; }
  html, body { width: 1200px; height: 894px; overflow: hidden; }
  body {
    background: radial-gradient(ellipse at 60% 40%, #b4b4b4 0%, var(--backdrop) 80%);
    position: relative;
    font-family: "Play", sans-serif;
  }
  .card {
    position: absolute;
    width: 600px;
    height: 343px;
    border-radius: 3px;
    overflow: hidden;
    box-shadow: 0 14px 30px rgba(0,0,0,0.28);
  }

  /* Front: brand face */
  .card-front {
    left: 560px; top: 90px;
    background: radial-gradient(ellipse at 55% 60%, var(--white) 0%, var(--card-white) 45%, var(--card-silver) 100%);
  }
  .brand-lockup {
    position: absolute;
    right: 46px; top: 175px;
    text-align: right;
  }
  .brand-name {
    font-family: "Play", sans-serif;
    font-weight: 400;
    color: var(--brand-blue-deep);
    font-size: 40px;
    line-height: 1;
    letter-spacing: 3px;
    text-transform: uppercase;
  }
  .brand-name .line { display: block; }
  .brand-tagline {
    margin-top: 12px;
    font-family: "Cinzel", serif;
    font-size: 15px;
    letter-spacing: 2px;
    color: var(--ink-soft);
    text-transform: uppercase;
    white-space: nowrap;
  }

  /* Back: contact face */
  .card-back {
    left: 60px; top: 470px;
    background: var(--brand-blue);
  }
  .card-back .band-top,
  .card-back .band-bottom {
    position: absolute; left: 0; width: 100%;
    background: linear-gradient(180deg, var(--brand-blue) 0%, var(--brand-blue-deep) 100%);
  }
  .band-top { top: 0; height: 62px; }
  .band-bottom { bottom: 0; height: 62px; }
  .rule {
    position: absolute; left: 0; width: 100%; height: 7px;
    background: var(--bar-black);
  }
  .rule-top { top: 62px; }
  .rule-bottom { bottom: 62px; }
  .info-panel {
    position: absolute; left: 0; right: 0; top: 69px; bottom: 69px;
    background: radial-gradient(ellipse at 50% 50%, var(--white) 0%, #ececec 70%, var(--card-silver) 100%);
  }
  .person-name {
    position: absolute; left: 34px; top: 18px;
    font-family: "Oswald", sans-serif;
    font-weight: 500;
    font-size: 46px;
    line-height: 1;
    letter-spacing: 1px;
    color: var(--ink);
    text-transform: uppercase;
    white-space: nowrap;
  }
  .title-bar {
    position: absolute; left: 0; top: 78px;
    width: 262px; height: 62px;
    background: var(--bar-black);
    padding: 8px 0 0 34px;
    color: var(--white);
  }
  .person-title {
    font-size: 13px;
    letter-spacing: 1.5px;
    text-transform: uppercase;
    border-bottom: 1px solid rgba(255,255,255,0.6);
    padding-bottom: 6px;
    margin-right: 14px;
    white-space: nowrap;
  }
  .website {
    margin-top: 6px;
    font-size: 10px;
    letter-spacing: 0.5px;
    white-space: nowrap;
  }
  .contact-list {
    position: absolute; left: 300px; top: 20px;
    list-style: none;
  }
  .contact-item {
    display: flex; align-items: center;
    gap: 12px;
    margin-bottom: 18px;
    font-size: 13px;
    line-height: 1.3;
    color: var(--ink);
    white-space: nowrap;
  }
  .contact-icon {
    flex: none;
    width: 34px; height: 34px;
    border-radius: 50%;
    background: var(--ink);
    display: flex; align-items: center; justify-content: center;
  }
  .contact-icon svg { width: 18px; height: 18px; }
</style>
</head>
<body>

<section class="card card-front" aria-label="Business card front">
  <div class="brand-lockup">
    <div class="brand-name"><span class="line">Harborline</span><span class="line">Talent</span></div>
    <div class="brand-tagline">Building teams that deliver</div>
  </div>
</section>

<section class="card card-back" aria-label="Business card back">
  <div class="band-top"></div>
  <div class="rule rule-top"></div>
  <div class="info-panel">
    <h1 class="person-name">John Doe</h1>
    <div class="title-bar">
      <p class="person-title">General Manager</p>
      <p class="website">www.harborlinetalent-example.com</p>
    </div>
    <ul class="contact-list">
      <li class="contact-item">
        <span class="contact-icon">
          <svg viewBox="0 0 20 20" aria-hidden="true"><path d="M10 3 L2 10 H5 V17 H15 V10 H18 Z" fill="#fff"/><rect x="8.5" y="12" width="3" height="5" fill="#2b2b2b"/></svg>
        </span>
        <span>214 9th floor, Quay<br>Lantern Road HBV</span>
      </li>
      <li class="contact-item">
        <span class="contact-icon">
          <svg viewBox="0 0 20 20" aria-hidden="true"><rect x="6" y="2" width="8" height="16" rx="1.5" fill="#fff"/><rect x="7.3" y="4" width="5.4" height="10" fill="#2b2b2b"/><circle cx="10" cy="16" r="0.9" fill="#2b2b2b"/></svg>
        </span>
        <span>012 555 0147</span>
      </li>
      <li class="contact-item">
        <span class="contact-icon">
          <svg viewBox="0 0 20 20" aria-hidden="true"><rect x="3" y="5" width="14" height="10" fill="#fff"/><path d="M3 5 L10 11 L17 5" fill="none" stroke="#2b2b2b" stroke-width="1.2"/></svg>
        </span>
        <span>name@harborlinetalent-example.com</span>
      </li>
    </ul>
  </div>
  <div class="rule rule-bottom"></div>
  <div class="band-bottom"></div>
</section>

</body>
</html>
```